Business Card Design

My company is an online based training service targeted at individuals who want to learn how to consistently make money at online tournament poker.

The training takes place online using skype and is extremely easy to use.

Final design should communicate that my business offers online tournament poker coaching from one of the most successful online tournament poker players in Scotland and the UK.

Further information can be found @ http://www.mendmyhand.net/

Industry/Entity Type

Training

Contact Information for Business Card

- 'Learn from one of the best online tournament poker players in Scotland and the UK' (or something similar)
- Previous winnings
Reference: http://www.mendmyhand.net/

Requirements
Must have
• MendMyHand.net
Nice to have
• A similar look or feel to my website (http://www.mendmyhand.net/)

```html
<!DOCTYPE html>
<html lang="en">
<head>
<meta charset="utf-8">
<title>MendMyHand.net – Business Cards</title>
<link href="https://fonts.googleapis.com/css2?family=Lora:wght@400;600&display=swap" rel="stylesheet">
<style>
  :root {
    --canvas: #e7e5e1;
    --felt: #1f4a2a;
    --felt-dark: #163a20;
    --panel: #141414;
    --panel-edge: #2b2b2b;
    --gold: #f2b61c;
    --ink: #f1efe9;
    --chip-red: #8c1a22;
    --chip-gold: #d7a21a;
  }
  * { box-sizing: border-box; margin: 0; padding: 0; }
  html, body {
    width: 1200px; height: 873px; overflow: hidden;
    background: var(--canvas);
    font-family: "Lora", Georgia, serif;
  }
  .canvas {
    width: 1200px; height: 873px;
    display: flex; align-items: center; justify-content: center; gap: 40px;
  }
  .card {
    position: relative;
    width: 540px; height: 309px;
    background: var(--felt);
    border-radius: 6px;
    box-shadow: 0 6px 18px rgba(0,0,0,.25);
    overflow: hidden;
  }
  .card__illustration {
    position: absolute; left: 0; top: 0; bottom: 0; width: 160px;
    background: radial-gradient(circle at 40% 45%, var(--chip-red) 0%, var(--chip-gold) 30%, var(--felt-dark) 75%);
    opacity: .85;
  }
  .card__panel {
    position: absolute;
    background: var(--panel);
    border: 1px solid var(--panel-edge);
    border-radius: 18px;
    display: flex; flex-direction: column; align-items: center; justify-content: center;
    text-align: center; color: var(--ink);
  }
  .card--back .card__panel { left: 170px; right: 16px; top: 16px; bottom: 16px; padding: 0 26px; }
  .card--front .card__panel { left: 16px; right: 16px; top: 16px; bottom: 16px; }

  .brand {
    display: flex; align-items: center; gap: 10px;
    color: var(--gold);
    font-weight: 600;
  }
  .brand__mark { width: 12px; height: 12px; border-radius: 50%; background: var(--gold); }
  .card--back .brand { font-size: 19px; margin-bottom: 14px; }
  .card--front .brand { font-size: 34px; margin-bottom: 22px; }
  .card--front .brand__mark { width: 18px; height: 18px; }

  .tagline { font-size: 15px; line-height: 1.45; }
  .divider { display: flex; gap: 10px; margin: 12px 0; }
  .divider span { width: 7px; height: 7px; border-radius: 50%; background: var(--gold); }
  .reference { font-size: 15px; line-height: 1.45; }
  .web { font-size: 15px; letter-spacing: .02em; }
</style>
</head>
<body>
<main class="canvas">
  <article class="card card--back">
    <div class="card__illustration" role="img" aria-label="Scattered poker chips and playing cards on green felt"></div>
    <div class="card__panel">
      <div class="brand"><span class="brand__mark"></span>MendMyHand.net</div>
      <p class="tagline">Learn from one of the best online tournament poker players in Scotland and the UK</p>
      <div class="divider"><span></span><span></span><span></span></div>
      <p class="reference">Previous winnings Reference:<br>www.mendmyhand.net</p>
    </div>
  </article>

  <article class="card card--front">
    <div class="card__panel">
      <div class="brand"><span class="brand__mark"></span>MendMyHand.net</div>
      <p class="web">www.mendmyhand.net</p>
    </div>
  </article>
</main>
</body>
</html>
```